Business Card Design and Stationary design for consulting firm

Harbourline Sourcing are looking for a new business card design and a design for their A4 letterhead / A4 invoices.

We are seeking to heavily increase our brand awareness and require a business card that's professional in appearance but also shows flare and innovation. A card design that people will remember.

About Us
Harbourline Sourcing are `The Sourcing Crew’.
Our mission is to be one of Australia’s greatest companies. Our aim is to help our customers achieve the best result from their purchasing experience.

Our Requirement:
• IMPACT! IMPACT! IMPACT!
• BUSINESS & PROFESSIONAL LOOKING

• Our business colours are orange, blue and green (See the logo attached).

We have provided an Art Design specification (attached) that needs to be followed for you to win the design. This also has the font, which is used on the logo.

We are after a two sided business card

Side One should have the:
The company Logo
The Sourcing Crew
www.harbourlinesourcing.com.au
Procure | Personnel | Probity & Privacy
Sydney | Melbourne | Adelaide | Brisbane

Side Two
Logo (optional)
Harbourline Sourcing (optional)
Employee details (details listed below)

The above format is our preferred option, but if you think you can come up with something better, feel free to put it forward.

We are leaving the design up to you, but it must incorporate the logo.

We will need a template that we can change the employee details on, as we will be adding more staff over the coming months.

The details below are for one employee per card with the same design.
------------------------

Employee Details:

Marcus Oldfield MBA, MMgmtStratProc
Principal Consultant
0412 356 917
Marcus@harbourlinesourcing.com.au

Brianna Tolhurst
Consulting Manager
0431 629 084
Brianna@harbourlinesourcing.com.au

Our website is www.harbourlinesourcing.com.au

The Letterhead / invoice needs to incorporate:
the company Logo
The Sourcing Crew
Sydney | Melbourne | Adelaide | Brisbane but otherwise the design is over to you.

This file needs to be delivered in word format as other detail will be added to the documents.

We look forward to you award winning designs. If you require any further information please feel free to contact us.

Regards
Harbourline Sourcing

Target Market(s)

Our Target market is companies with 80+ employees. The market we segment is heavily male based, between the ages of 35-55 years of age.

Industry/Entity Type

Consulting

Contact Information for Business Card

See Project Description

Font styles to use
Other font styles liked:
• See Art Specification

Requirements
Must have
• Company Colours, See Project Description
Should not have
• Be outside the Art specification guidelines

```html
<!DOCTYPE html>
<html lang="en">
<head>
<meta charset="utf-8">
<title>Harbourline Sourcing – Business Card</title>
<link rel="stylesheet" href="https://fonts.googleapis.com/css2?family=Source+Sans+3:wght@400;600;700&display=swap">
<style>
  :root {
    --stage: #161616;
    --stage-top: #262626;
    --card-white: #ffffff;
    --brand-blue: #1a73c0;
    --brand-sky: #22a6e0;
    --brand-deep: #1876c3;
    --ink-dark: #2b2b2b;
    --ink-grey: #9a9a9a;
    --ink-white: #ffffff;
  }
  * { box-sizing: border-box; margin: 0; padding: 0; }
  html, body { width: 1200px; height: 900px; overflow: hidden; }
  body {
    background: linear-gradient(180deg, var(--stage-top) 0%, var(--stage) 60%, #0a0a0a 100%);
    font-family: "Source Sans 3", "Myriad Pro", sans-serif;
    position: relative;
  }
  .card {
    position: absolute;
    top: 306px;
    width: 440px;
    height: 271px;
    border-radius: 12px;
    overflow: hidden;
  }
  .card--front { left: 149px; background: var(--card-white); }
  .card--back {
    left: 608px;
    background: linear-gradient(180deg, var(--brand-sky) 0%, var(--brand-deep) 100%);
    color: var(--ink-white);
    text-align: center;
  }

  /* front */
  .brand-lockup {
    position: absolute;
    left: 20px;
    top: 95px;
    width: 170px;
    text-align: center;
    color: var(--ink-dark);
    font-weight: 700;
    font-size: 19px;
    line-height: 1.15;
    letter-spacing: 0.5px;
  }
  .brand-lockup .brand-dot {
    display: block;
    width: 38px; height: 38px;
    margin: 0 auto 10px;
    border-radius: 50%;
    background: var(--brand-blue);
  }
  .staff {
    position: absolute;
    left: 206px;
    top: 80px;
  }
  .staff__name { color: var(--brand-blue); font-weight: 600; font-size: 17px; line-height: 20px; }
  .staff__quals { color: var(--ink-dark); font-weight: 600; font-size: 12.5px; line-height: 16px; }
  .staff__role { color: var(--ink-grey); font-size: 14.5px; line-height: 22px; margin-top: 2px; }
  .contact { margin-top: 17px; list-style: none; }
  .contact li {
    display: flex; align-items: center; gap: 6px;
    color: var(--ink-grey); font-size: 12.5px; line-height: 16px;
  }
  .contact svg { width: 10px; height: 10px; fill: var(--brand-blue); flex: none; }
  .cities {
    position: absolute;
    left: 0; right: 0; top: 221px;
    text-align: center;
    color: var(--brand-blue);
    font-weight: 600;
    font-size: 16.5px;
  }

  /* back */
  .brand-lockup--large {
    position: absolute;
    left: 0; right: 0; top: 52px;
    color: var(--ink-white);
    font-weight: 700;
    font-size: 26px;
    letter-spacing: 0.5px;
  }
  .brand-lockup--large .brand-dot {
    display: block;
    width: 54px; height: 54px;
    margin: 0 auto 14px;
    border-radius: 50%;
    background: var(--ink-white);
  }
  .web { position: absolute; left: 0; right: 0; top: 195px; font-size: 13px; }
  .services { position: absolute; left: 0; right: 0; top: 219px; font-size: 14.5px; }
</style>
</head>
<body>
  <section class="card card--front" aria-label="Business card front">
    <div class="brand-lockup"><span class="brand-dot"></span>Harbourline Sourcing</div>
    <div class="staff">
      <p class="staff__name">Marcus Oldfield</p>
      <p class="staff__quals">MBA, MMgmtStratProc</p>
      <p class="staff__role">Principal Consultant</p>
      <ul class="contact">
        <li>
          <svg viewBox="0 0 10 10" aria-hidden="true"><path d="M2 0.5 L3.6 2.6 L2.7 3.6 C3.3 5 4.9 6.6 6.4 7.3 L7.4 6.4 L9.5 8 L8.4 9.5 C4.6 9.2 0.8 5.4 0.5 1.6 Z"/></svg>
          0412 356 917
        </li>
        <li>
          <svg viewBox="0 0 10 10" aria-hidden="true"><path d="M0.5 2 H9.5 V8.5 H0.5 Z M1 2.5 L5 5.6 L9 2.5" stroke="#fff" stroke-width="0.8"/></svg>
          Marcus@harbourlinesourcing.com.au
        </li>
      </ul>
    </div>
    <p class="cities">Sydney | Melbourne | Adelaide | Brisbane</p>
  </section>

  <section class="card card--back" aria-label="Business card back">
    <div class="brand-lockup--large"><span class="brand-dot"></span>Harbourline Sourcing</div>
    <p class="web">www.harbourlinesourcing.com.au</p>
    <p class="services">Procure | Personnel | Probity &amp; Privacy</p>
  </section>
</body>
</html>
```